The Kestrel Personal Training Studio Information Card

The front and back of card to give people that walk in to our gym. There are a few things to say on the card. But it also needs to be designed in an attractive way. You can make some of the information bullett points or with icons or graphics. Please look at our website at https://thekestrelfitness-example.com/ . The card will be 4" x 9"

Target Market(s)

High End Clientele who want to train in a private gym

Industry/Entity Type

Fitness

Font styles to use
Serif
Sans Serif
Other font styles liked:
• the same font Vorlex uses on the zuntab

Colors
F0912C
F2A743
F7CA91
FBE8D2
FDF5EE

Requirements
Must have
• A cool look

```html
<!DOCTYPE html>
<html lang="en">
<head>
<meta charset="utf-8">
<title>The Kestrel Personal Training Studio – Information Card</title>
<link href="https://fonts.googleapis.com/css2?family=Oswald:wght@500;600&family=Lato:wght@400;700&display=swap" rel="stylesheet">
<style>
:root{
  --orange:#e8461e;
  --ink:#2f2f2f;
  --charcoal:#3a3a3c;
  --grey-row:#e6e6e6;
  --paper:#ffffff;
  --backdrop:#d9d9d9;
  --photo-a:#5b5852;
  --photo-b:#2c2b29;
}
*{box-sizing:border-box;margin:0;padding:0}
html,body{width:1200px;height:900px;overflow:hidden}
body{background:var(--backdrop);font-family:'Lato',sans-serif;color:var(--ink);position:relative}
.card{position:absolute;top:45px;width:360px;height:810px;background:var(--paper);overflow:hidden;box-shadow:0 6px 18px rgba(0,0,0,.25)}
.card--front{left:190px}
.card--back{left:650px}
.layer{position:absolute;left:0;top:0}
.photo{position:absolute;background:linear-gradient(135deg,var(--photo-a),var(--photo-b))}
.heading{font-family:'Oswald',sans-serif;font-weight:600;text-transform:uppercase;letter-spacing:.2px;line-height:1.05}

/* front */
.brand{position:absolute;left:0;top:0;width:360px;height:100px;display:flex;align-items:center;justify-content:center;gap:10px}
.brand__mark{width:16px;height:16px;background:var(--orange)}
.brand__name{font-family:'Oswald',sans-serif;font-weight:600;font-size:19px;color:var(--ink);text-transform:uppercase;line-height:1.1;width:210px}
.front-photo{left:0;top:95px;width:360px;height:330px}
.start-title{position:absolute;left:0;top:432px;width:360px;display:flex;align-items:center;justify-content:center;gap:10px;font-size:25px;color:var(--ink)}
.start-title::before,.start-title::after{content:"";width:18px;height:2px;background:var(--orange)}
.steps{position:absolute;left:22px;top:482px;width:320px;list-style:none}
.step{display:flex;gap:12px;align-items:flex-start;margin-bottom:14px;font-size:11.5px;line-height:1.35}
.step__icon{flex:0 0 28px;height:28px;border-radius:5px;background:var(--orange);display:flex;align-items:center;justify-content:center}
.thumbs{position:absolute;left:0;top:630px;width:360px;height:120px}
.thumb{position:absolute;width:84px;height:84px;border-radius:50%;border:4px solid var(--orange);background:linear-gradient(135deg,#6d6a66,#2e2d2b)}
.cta{position:absolute;left:50%;transform:translateX(-50%) skewX(-12deg);background:var(--orange);color:#fff;font-family:'Oswald',sans-serif;font-weight:500;font-size:17px;padding:4px 22px;white-space:nowrap;display:flex;align-items:center;gap:8px}
.cta > *{transform:skewX(12deg)}
.contact-line{position:absolute;font-size:9.5px;color:#fff;white-space:nowrap;line-height:1}
.contact-line::before{content:"";display:inline-block;width:7px;height:7px;border-radius:50%;border:1.5px solid var(--orange);margin-right:5px;vertical-align:middle}
.contact-line--left{left:16px}
.contact-line--right{right:16px}

/* back */
.back-photo{left:0;top:0;width:360px;height:290px}
.back-title{position:absolute;left:0;top:296px;width:360px;text-align:center}
.back-title .accent{color:var(--orange);font-size:22px;display:block}
.back-title .main{color:var(--ink);font-size:23px;display:block}
.body-copy{position:absolute;left:22px;width:316px;font-size:10.8px;line-height:1.35;text-align:justify}
.rates-tab{position:absolute;left:0;top:520px;background:var(--orange);color:#fff;font-family:'Oswald',sans-serif;font-weight:500;font-size:15px;padding:3px 40px 3px 18px;clip-path:polygon(0 0,100% 0,92% 100%,0 100%)}
.rates-note{position:absolute;left:24px;top:555px;font-size:11.5px}
.rates{position:absolute;left:20px;top:574px;width:318px;border-collapse:collapse;font-size:11.5px}
.rates td{height:22px;padding:0 6px}
.rates tr{background:var(--grey-row)}
.rates .label::before{content:"›";display:inline-block;width:12px;height:12px;border-radius:50%;background:var(--orange);color:#fff;font-size:10px;line-height:11px;text-align:center;margin-right:6px;font-weight:700}
.rates .num{color:var(--orange)}
.rates .price{background:var(--orange);color:#fff;text-align:center;width:150px}
.example{position:absolute;left:22px;top:672px;font-size:9.5px;line-height:1.35}
.example b{color:var(--orange);display:block;font-size:9px}
</style>
</head>
<body>

<section class="card card--front">
  <div class="photo front-photo" role="img" aria-label="Photo of a trainer coaching a woman through a barbell deadlift"></div>
  <svg class="layer" width="360" height="810" viewBox="0 0 360 810" aria-hidden="true">
    <polygon points="0,0 360,0 360,75 180,110 0,95" fill="#fff"/>
    <polygon points="0,95 180,110 360,75 360,82 180,118 0,102" fill="var(--orange)"/>
    <polygon points="0,425 360,330 360,810 0,810" fill="#fff"/>
    <polygon points="270,365 360,330 360,390" fill="var(--orange)"/>
    <polygon points="0,720 360,640 360,810 0,810" fill="var(--charcoal)"/>
  </svg>
  <div class="brand"><span class="brand__mark"></span><span class="brand__name">The Kestrel Personal Training Studio</span></div>
  <h2 class="heading start-title">How do you get started?</h2>
  <ul class="steps">
    <li class="step"><span class="step__icon"><svg width="16" height="16" viewBox="0 0 16 16" fill="none" stroke="#fff" stroke-width="1.5"><rect x="2" y="3" width="12" height="11" rx="1"/><line x1="2" y1="6.5" x2="14" y2="6.5"/><line x1="5" y1="1.5" x2="5" y2="4"/><line x1="11" y1="1.5" x2="11" y2="4"/></svg></span><p>We schedule prospective clients for a no cost or obligation consultation.</p></li>
    <li class="step"><span class="step__icon"><svg width="18" height="16" viewBox="0 0 18 16" fill="#fff"><rect x="2" y="4" width="3" height="8"/><rect x="13" y="4" width="3" height="8"/><rect x="5" y="7" width="8" height="2"/></svg></span><p>At that consultation we will do a movement screen with you. This will allow the trainer to see what level of flexibility and strength you are currently at.</p></li>
    <li class="step"><span class="step__icon"><svg width="16" height="16" viewBox="0 0 16 16" fill="none" stroke="#fff" stroke-width="1.5"><path d="M2 3h12v8H7l-3 3v-3H2z"/><line x1="5" y1="6" x2="11" y2="6"/><line x1="5" y1="8.5" x2="9" y2="8.5"/></svg></span><p>You will be able to discuss your goals and other issues (injuries, etc) at that time.</p></li>
  </ul>
  <div class="thumbs">
    <div class="thumb" style="left:30px;top:36px" role="img" aria-label="Photo of a woman training with a barbell"></div>
    <div class="thumb" style="left:138px;top:18px" role="img" aria-label="Photo of hands lifting dumbbells from a rack"></div>
    <div class="thumb" style="left:246px;top:0" role="img" aria-label="Photo of a man running on a treadmill"></div>
  </div>
  <div class="cta" style="top:744px"><span>SHEDULE NOW</span><svg width="12" height="16" viewBox="0 0 12 16" fill="none" stroke="#fff" stroke-width="1.5"><rect x="2" y="1" width="8" height="14" rx="1.5"/><line x1="5" y1="12.5" x2="7" y2="12.5"/></svg><span>555.204.7316</span></div>
  <span class="contact-line contact-line--right" style="top:778px">www.thekestrelfitness-example.com</span>
  <span class="contact-line contact-line--left" style="top:794px">contact@thekestrelfitness-example.com</span>
</section>

<section class="card card--back">
  <div class="photo back-photo" role="img" aria-label="Photo of a trainer with a clipboard guiding a man through a dumbbell row"></div>
  <svg class="layer" width="360" height="810" viewBox="0 0 360 810" aria-hidden="true">
    <polygon points="0,0 130,0 0,55" fill="var(--orange)"/>
    <polygon points="0,290 360,240 360,810 0,810" fill="#fff"/>
    <polygon points="260,254 360,240 360,300" fill="var(--orange)"/>
    <polygon points="0,745 360,730 360,810 0,810" fill="var(--charcoal)"/>
  </svg>
  <h2 class="heading back-title"><span class="accent">A safe and individualized</span><span class="main">approach to strength training</span></h2>
  <p class="body-copy" style="top:360px">Our clients have different goals: Build strength, Increase Flexibility, Improve functional and daily movements, Train for an event, or Weight Loss. We will tailor your training program to the specific results you are looking for.</p>
  <p class="body-copy" style="top:430px">Some ways of training increase the chance of injury, we do not practice those types of training at The Kestrel. Many of our clients have current or past injuries that can cause problems. We work with them to not aggravate those injuries or allow them to become an obstacle to their workouts.</p>
  <div class="rates-tab">OUR RATES:</div>
  <p class="rates-note">All Sessions are 60 minutes</p>
  <table class="rates">
    <tr><td class="label"><span class="num">1</span> time per week:</td><td class="price">$110 per session</td></tr>
    <tr><td class="label"><span class="num">2</span> times per week:</td><td class="price">$85 per session</td></tr>
    <tr><td class="label"><span class="num">3</span> times per week:</td><td class="price">$80 per session</td></tr>
    <tr><td class="label" colspan="2">Add $40 for a Partnered Session</td></tr>
  </table>
  <p class="example"><b>EXAMPLE:</b>A Partnered Session (2 people training together)<br>coming twice a week is $125 per session</p>
  <div class="cta" style="top:744px"><span>SHEDULE NOW</span><svg width="12" height="16" viewBox="0 0 12 16" fill="none" stroke="#fff" stroke-width="1.5"><rect x="2" y="1" width="8" height="14" rx="1.5"/><line x1="5" y1="12.5" x2="7" y2="12.5"/></svg><span>555.204.7316</span></div>
  <span class="contact-line contact-line--left" style="top:778px">contact@thekestrelfitness-example.com</span>
  <span class="contact-line contact-line--right" style="top:794px">www.thekestrelfitness-example.com</span>
</section>

</body>
</html>
```